Kivo Campaign Flyer

Tobu is a not-for-profit college planning organization serving the students of Louisiana's public and private high schools.

Tobu will offer Louisiana high school seniors, aged 17-19, the opportunity to compete for a free Kivo by registering and completing a brief survey on our webpage by March 1st to be eligible for this random drawing.

As a result, we are soliciting designs for an age-appropriate, innovative design idea to promote this program. The winning design will be printed as a 5-3/4” x 7-3/4” flyer which will be distributed to Louisiana high school seniors and guidance counselors, encouraging them to participate.

```html
<!DOCTYPE html>
<html lang="en">
<head>
<meta charset="utf-8">
<title>Kivo Campaign Flyer – Tobu</title>
<link href="https://fonts.googleapis.com/css2?family=Bebas+Neue&family=Oswald:wght@500;600&display=swap" rel="stylesheet">
<style>
  :root {
    --paper: #ffffff;
    --ink: #111111;
    --headline: #ffffff;
    --lime: #a6f500;
    --lime-bright: #c8ff1a;
    --lime-deep: #6fbf00;
    --sun: #fff200;
    --brand-navy: #1f2a7a;
    --brand-green: #9ed61c;
  }
  html, body {
    margin: 0;
    padding: 0;
    overflow: hidden;
    background: var(--paper);
  }
  .flyer {
    position: relative;
    width: 890px;
    height: 1200px;
    overflow: hidden;
    background: var(--paper);
    font-family: "Oswald", "Arial Narrow", sans-serif;
    color: var(--ink);
  }
  .flyer__backdrop {
    position: absolute;
    inset: 0;
  }
  .intro {
    position: absolute;
    top: 8px;
    left: 0;
    width: 100%;
    margin: 0;
    text-align: center;
    font-weight: 500;
    font-size: 47px;
    line-height: 62px;
  }
  .intro__line--caps { text-transform: uppercase; }
  .headline {
    position: absolute;
    left: 0;
    width: 100%;
    margin: 0;
    text-align: center;
    font-family: "Bebas Neue", "Oswald", sans-serif;
    font-weight: 400;
    color: var(--headline);
    text-shadow: 0 0 18px rgba(0, 0, 0, 0.45), 0 4px 10px rgba(0, 0, 0, 0.35);
  }
  .headline--win { top: 150px; font-size: 230px; line-height: 230px; letter-spacing: 4px; }
  .headline--prize { top: 345px; font-size: 300px; line-height: 300px; letter-spacing: 6px; }
  .instructions {
    position: absolute;
    right: 16px;
    top: 642px;
    margin: 0;
    text-align: right;
    font-weight: 500;
    font-size: 50px;
    line-height: 63px;
  }
  .eligibility {
    position: absolute;
    left: 452px;
    top: 1122px;
    margin: 0;
    font-weight: 500;
    font-size: 38px;
    line-height: 56px;
  }
  .brand {
    position: absolute;
    left: 20px;
    top: 960px;
    display: flex;
    align-items: center;
    gap: 12px;
  }
  .brand__dot {
    width: 44px;
    height: 44px;
    border-radius: 50%;
    background: var(--brand-green);
  }
  .brand__name {
    font-weight: 500;
    font-size: 72px;
    line-height: 1;
    color: var(--brand-navy);
  }
</style>
</head>
<body>
<main class="flyer">
  <svg class="flyer__backdrop" width="890" height="1200" viewBox="0 0 890 1200" aria-hidden="true">
    <defs>
      <linearGradient id="lime-field" x1="0" y1="0" x2="1" y2="1">
        <stop offset="0" stop-color="var(--sun)"/>
        <stop offset="0.3" stop-color="var(--lime-bright)"/>
        <stop offset="0.6" stop-color="var(--lime)"/>
        <stop offset="1" stop-color="var(--lime-deep)"/>
      </linearGradient>
      <linearGradient id="edge-shade" x1="0" y1="0" x2="1" y2="0">
        <stop offset="0" stop-color="#ffffff"/>
        <stop offset="1" stop-color="#9a9a9a"/>
      </linearGradient>
    </defs>
    <polygon class="field" fill="url(#lime-field)"
      points="0,148 890,148 890,630 430,630 805,1110 360,1110 0,650"/>
    <polygon class="field-fold" fill="#000" opacity="0.08"
      points="0,148 110,148 700,630 430,630"/>
    <polygon class="footer-edge" fill="url(#edge-shade)"
      points="360,1110 890,1110 890,1122 370,1122"/>
  </svg>

  <h2 class="intro">
    <span class="intro__line">Louisiana high school seniors,</span><br>
    <span class="intro__line intro__line--caps">Just fill out a simple survey and</span>
  </h2>

  <h1 class="headline headline--win">WIN AN</h1>
  <p class="headline headline--prize">KIVO</p>

  <p class="instructions">
    Fill in the survey on<br>
    www.asktobu.org<br>
    by March 1st<br>
    to WIN
  </p>

  <div class="brand">
    <span class="brand__dot"></span>
    <span class="brand__name">Tobu</span>
  </div>

  <p class="eligibility">For The Ages of 17-19</p>
</main>
</body>
</html>
```